Poster for Tradesmen Website

We had a soft launch of our website. The site brings together tradesmen jobseekers and customers to one virtual location. The website serves Australian market. To clearly understand what we mean please visit www.quellmark.com.au. For our future promotional campaign we intend to use poster which we intend to distribute in trade exhibits and in recruitment offices.
Color and Poster Design Content: - Very light blue is the predominant color of the website. The design is not limited on this color. They are free to explore other color if they think that will effectively convey the message of the poster. Presently our website uses images showing tradesmen in action as well as the customers. Designers can use these images or use other image in their design which will best suit their design
Size: - We are looking at poster printed A3 size, but the design should not limit their target size on A3 (it should be versatile, insure that the file format for your design support large-format printing without being pixilated) since we also want it printed in vinyl as stand-alone banner (example: 1200 x 1700 mm approx) that will be used in trade exhibits.
Message of the Poster:
For our first marketing campaign we want to join a trade expo which will be held on the last week of May 2012. For this expo we need a poster and a stand-alone banner to be displayed on our booth. The poster should convey the following message:
a) that a new website has been launched
b) that the website brings together tradesmen, customers and jobseekers to one virtual location
c) that for tradesmen the website is a venue to advertise their business
d) that for customers, it will make the task of finding the right tradies much easier
e) that for jobseekers the site is one way of finding a job by just posting their resume and potential employers can view the summary of their qualification and send notification if they are interested on a particular jobseeker.
Images:
We don't have any other high resolution images Except for the images that we used on our website. We got those images online. Besides, we are not sure what particular image will be appropriate for the poster. As the designer and the creative artist as well, you are free to use whatever images that you think is appropriate for the your design. We think any images (not necessarily tradesmen images) can be used as long as it can strongly convey our message. Again, as the creative artist it is up to you to decide what image is/are appropriate. The only thing we can tell you guys is that we can tell a good/excellent design when we see one.
Logo:
We don't have a logo yet for our website. For the purpose of this poster you can use the font used on website name:
quellmark.com.au
quell {font-family:Arial, Helvetica, sans-serif; color:#407FC0;}
mark.com.au {font-family:Arial, Helvetica, sans-serif; color:#00007F;}
Age group: 18 - 65, Gender: male-female, Education: any
Marketing

```html
<!DOCTYPE html>
<html lang="en">
<head>
<meta charset="utf-8">
<title>Quellmark launch – banner and poster</title>
<link rel="stylesheet" href="https://fonts.googleapis.com/css2?family=Arimo:wght@400;700&display=swap">
<style>
  :root {
    --board-yellow: #ffdd00;
    --panel-black: #000000;
    --band-navy: #003478;
    --text-white: #ffffff;
    --address-cyan: #12a8dc;
    --sky-deep: #8a1a0a;
    --sky-red: #d8300c;
    --sky-orange: #f07a12;
    --sky-gold: #f6a81a;
  }
  * { box-sizing: border-box; margin: 0; padding: 0; }
  html, body { width: 1200px; height: 800px; overflow: hidden; }
  body {
    background: var(--board-yellow);
    font-family: "Arimo", Arial, sans-serif;
    color: var(--text-white);
    position: relative;
  }
  .artboard {
    position: absolute;
    top: 30px;
    width: 522px;
    height: 740px;
    background: var(--panel-black);
    overflow: hidden;
  }
  .artboard--banner { left: 73px; }
  .artboard--poster { left: 605px; overflow: visible; }

  .sunset-scene {
    position: absolute;
    left: 0; top: 0;
    width: 522px;
    height: 500px;
    background: linear-gradient(to bottom,
      var(--sky-deep) 0%,
      var(--sky-red) 35%,
      var(--sky-orange) 58%,
      var(--sky-gold) 70%,
      #4a1204 84%,
      var(--panel-black) 100%);
  }

  .site-address {
    position: absolute;
    left: 0; width: 100%;
    text-align: center;
    font-weight: 700;
    white-space: nowrap;
  }
  .artboard--banner .site-address {
    top: 506px;
    font-size: 42px;
  }
  .launch-band {
    position: absolute;
    left: 2px; right: 1px;
    top: 572px;
    height: 26px;
    background: var(--band-navy);
    font-weight: 700;
    font-size: 22px;
    line-height: 26px;
    text-align: center;
    white-space: nowrap;
  }

  .message-list {
    position: absolute;
    left: 42px;
    top: 446px;
    width: 452px;
    list-style: none;
  }
  .message-list li {
    position: relative;
    padding-left: 27px;
    font-size: 12px;
    line-height: 15px;
    margin-bottom: 12px;
  }
  .message-list li.message--lead {
    font-size: 22px;
    font-weight: 700;
    line-height: 24px;
    padding-left: 29px;
    margin-bottom: 11px;
    white-space: nowrap;
  }
  .message-list li:nth-child(3),
  .message-list li:nth-child(4) { margin-bottom: 17px; }
  .message-list li.message--justified { text-align: justify; }
  .bullet-arrow {
    position: absolute;
    left: 0; top: 3px;
    width: 10px; height: 9px;
  }
  .message--lead .bullet-arrow { top: 8px; }

  .address-band {
    position: absolute;
    left: -1px;
    width: 523px;
    top: 662px;
    height: 49px;
    background: var(--band-navy);
    font-size: 38px;
    font-weight: 700;
    line-height: 49px;
    text-align: center;
    white-space: nowrap;
  }
  .address-band__tail { color: var(--address-cyan); }

  .board-label {
    position: absolute;
    top: 667px;
    height: 23px;
    background: var(--panel-black);
    font-size: 16px;
    line-height: 23px;
    padding: 0 6px;
  }
  .board-label--banner { left: 4px; width: 69px; }
  .board-label--poster { left: 1128px; width: 67px; }
</style>
</head>
<body>
  <section class="artboard artboard--banner">
    <div class="sunset-scene" role="img" aria-label="Photo: silhouette of a construction worker raising both fists between tower cranes against a red and orange sunset"></div>
    <p class="site-address">www.quellmark.com.au</p>
    <p class="launch-band">that a new website has been launched</p>
  </section>

  <section class="artboard artboard--poster">
    <div class="sunset-scene" role="img" aria-label="Photo: silhouette of a construction worker raising both fists between tower cranes against a red and orange sunset"></div>
    <ul class="message-list">
      <li class="message--lead">
        <svg class="bullet-arrow" viewBox="0 0 10 9" aria-hidden="true"><g fill="#fff"><circle cx="1.5" cy="1.5" r="1.3"/><circle cx="1.5" cy="4.5" r="1.3"/><circle cx="1.5" cy="7.5" r="1.3"/><circle cx="5" cy="3" r="1.3"/><circle cx="5" cy="6" r="1.3"/><circle cx="8.5" cy="4.5" r="1.3"/></g></svg>
        that a new website has been launched
      </li>
      <li>
        <svg class="bullet-arrow" viewBox="0 0 10 9" aria-hidden="true"><g fill="#fff"><circle cx="1.5" cy="1.5" r="1.3"/><circle cx="1.5" cy="4.5" r="1.3"/><circle cx="1.5" cy="7.5" r="1.3"/><circle cx="5" cy="3" r="1.3"/><circle cx="5" cy="6" r="1.3"/><circle cx="8.5" cy="4.5" r="1.3"/></g></svg>
        that the website brings together tradesmen, customers and jobseekers to one virtual location
      </li>
      <li>
        <svg class="bullet-arrow" viewBox="0 0 10 9" aria-hidden="true"><g fill="#fff"><circle cx="1.5" cy="1.5" r="1.3"/><circle cx="1.5" cy="4.5" r="1.3"/><circle cx="1.5" cy="7.5" r="1.3"/><circle cx="5" cy="3" r="1.3"/><circle cx="5" cy="6" r="1.3"/><circle cx="8.5" cy="4.5" r="1.3"/></g></svg>
        that for tradesmen the website is a venue to advertise their business
      </li>
      <li>
        <svg class="bullet-arrow" viewBox="0 0 10 9" aria-hidden="true"><g fill="#fff"><circle cx="1.5" cy="1.5" r="1.3"/><circle cx="1.5" cy="4.5" r="1.3"/><circle cx="1.5" cy="7.5" r="1.3"/><circle cx="5" cy="3" r="1.3"/><circle cx="5" cy="6" r="1.3"/><circle cx="8.5" cy="4.5" r="1.3"/></g></svg>
        that for customers, it will make the task of finding the right tradies much easier
      </li>
      <li class="message--justified">
        <svg class="bullet-arrow" viewBox="0 0 10 9" aria-hidden="true"><g fill="#fff"><circle cx="1.5" cy="1.5" r="1.3"/><circle cx="1.5" cy="4.5" r="1.3"/><circle cx="1.5" cy="7.5" r="1.3"/><circle cx="5" cy="3" r="1.3"/><circle cx="5" cy="6" r="1.3"/><circle cx="8.5" cy="4.5" r="1.3"/></g></svg>
        that for jobseekers the site is one way of finding a job by just posting their resume and potential employers can view the summary of their qualification and send notification if they are interested on a particular jobseeker.
      </li>
    </ul>
    <p class="address-band">www.quell<span class="address-band__tail">mark.com.au</span></p>
  </section>

  <p class="board-label board-label--banner">Banner</p>
  <p class="board-label board-label--poster">Poster</p>
</body>
</html>
```